Worknest Background Picture

Professional WorkNest Banner Design for Individual in Architectural Industry

Hello talented designers,

I am looking for a creative and professional graphic designer to create a WorkNest banner for my personal profile. I am deeply involved in the architectural systems industry, specializing in innovative and sustainable building solutions.

What I'm Looking For:

Personal Branding: The banner should reflect my professional identity and role in the architectural systems industry. It should be more personal than corporate.

Visual Elements: Include imagery or abstract designs that represent architecture, innovation, and sustainability. The design should subtly hint at my industry expertise and areas of specialization.

Professional and Engaging: The design should be visually striking but maintain a professional look. It should engage viewers and encourage them to learn more about my professional background and skills.

File Requirements: The final design should be provided in a high-resolution JPEG or PNG format, fitting WorkNest's banner dimensions.

To Apply, Please Provide:

A summary of your design experience, especially with WorkNest banners or personal branding projects.
A portfolio showcasing your previous work, highlighting any designs related to personal branding or professional themes.
Your estimated timeline and budget for the project.
Selection Criteria:

Creativity in reflecting a personal professional brand.
Experience with individual professional branding.
Quality and relevance of the portfolio.
Competitive pricing and clear communication.
I am excited to see your creative approaches and look forward to collaborating to craft a banner that perfectly encapsulates my professional persona on WorkNest.

Thank you!

My worknest page:
worknest.example/in/morbevatki

Our website:

https://filebox.example/shared/folders/7qTbXwNpLmRzA2sKdHvYc94eoFjUi0BnM?usp=share_link

Some photos of our projects:

```html
<!DOCTYPE html>
<html lang="en">
<head>
<meta charset="utf-8">
<title>Morbe Vatki – WorkNest Banner</title>
<link href="https://fonts.googleapis.com/css2?family=Allura&family=Montserrat:wght@400;500;600;700&display=swap" rel="stylesheet">
<style>
  :root {
    --page: #f2f1ee;
    --banner-deep: #2f4f82;
    --banner-mid: #41659b;
    --banner-soft: #5679ac;
    --accent: #2fb7ea;
    --white: #ffffff;
    --hex-line: #7fa3d3;
  }
  * { box-sizing: border-box; margin: 0; padding: 0; }
  html, body { width: 1200px; height: 1200px; overflow: hidden; background: var(--page); }
  body { position: relative; font-family: "Montserrat", sans-serif; color: var(--white); }

  .banner {
    position: absolute; left: 40px; top: 460px;
    width: 1120px; height: 280px; overflow: hidden;
    background: linear-gradient(100deg, var(--banner-deep) 0%, var(--banner-mid) 45%, var(--banner-soft) 100%);
  }
  .banner-backdrop {
    position: absolute; inset: 0;
    background:
      repeating-linear-gradient(90deg, rgba(255,255,255,0.015) 0 38px, rgba(0,0,0,0.015) 38px 76px),
      repeating-linear-gradient(0deg, rgba(255,255,255,0.012) 0 30px, rgba(0,0,0,0.015) 30px 60px);
  }

  .brand { position: absolute; left: 28px; top: 34px; width: 110px; text-align: center; z-index: 2; }
  .brand-mark { width: 30px; height: 30px; border: 2px solid var(--white); margin: 0 auto 8px; }
  .brand-name { font-weight: 600; font-size: 15px; letter-spacing: 4px; line-height: 1.1; }
  .brand-name small { display: block; font-size: 5.5px; letter-spacing: 1.4px; margin-top: 2px; }

  .identity { position: absolute; left: 331px; top: 22px; width: 290px; z-index: 2; }
  .identity-name {
    font-family: "Allura", cursive; font-size: 66px; line-height: 1;
    color: var(--accent); white-space: nowrap;
  }
  .identity-role { display: flex; align-items: center; gap: 10px; margin-top: 2px; }
  .identity-role h1 { font-weight: 700; font-size: 27px; letter-spacing: 0.5px; line-height: 1; }
  .identity-role .rule { flex: 1; height: 2px; background: var(--white); }
  .identity-site { color: var(--accent); font-weight: 500; font-size: 15.5px; margin-top: 2px; }
  .identity-points { list-style: none; margin-top: 12px; font-size: 12px; line-height: 14.3px; white-space: nowrap; }
  .identity-points li span { color: var(--accent); margin-left: 4px; }

  .social { display: flex; justify-content: space-between; width: 282px; margin-top: 14px; font-size: 6.5px; font-weight: 700; white-space: nowrap; }
  .social-item { display: flex; align-items: center; gap: 3px; }
  .social-item i { display: block; width: 7px; height: 7px; background: var(--accent); }

  .collage { position: absolute; left: 0; top: 0; width: 1120px; height: 280px; z-index: 1; }
  .hex-outline { fill: none; stroke: var(--hex-line); stroke-width: 1.2; opacity: 0.7; }
  .hex-frame { stroke: var(--banner-mid); stroke-width: 4; }
</style>
</head>
<body>
  <section class="banner">
    <div class="banner-backdrop" role="img" aria-label="Faded photo of an apartment building facade in blue tint"></div>

    <svg class="collage" viewBox="0 0 1120 280">
      <defs>
        <linearGradient id="interior" x1="0" y1="0" x2="0" y2="1">
          <stop offset="0" stop-color="#a9c8e6"/><stop offset="0.55" stop-color="#e6edf2"/><stop offset="1" stop-color="#c9c2b6"/>
        </linearGradient>
        <linearGradient id="facade" x1="0" y1="0" x2="0" y2="1">
          <stop offset="0" stop-color="#3a5fa8"/><stop offset="1" stop-color="#24407a"/>
        </linearGradient>
        <linearGradient id="tower" x1="0" y1="0" x2="1" y2="1">
          <stop offset="0" stop-color="#9a8478"/><stop offset="1" stop-color="#6e6462"/>
        </linearGradient>
      </defs>
      <g transform="translate(24,0)">
        <polygon class="hex-outline" points="650,150 684,130 684,90 650,70 616,90 616,130"/>
        <polygon class="hex-outline" points="660,280 700,257 700,211 660,188 620,211 620,257"/>
        <polygon class="hex-outline" points="810,-10 830,2 830,25 810,37 790,25 790,2"/>

        <g role="img" aria-label="Photo of tower balconies against blue sky">
          <polygon class="hex-frame" fill="url(#facade)" points="844.5,-97 919,-54 919,32 844.5,75 770,32 770,-54"/>
          <polygon class="hex-frame" fill="url(#facade)" points="993.5,-97 1068,-54 1068,32 993.5,75 919,32 919,-54"/>
        </g>
        <g role="img" aria-label="Photo of a condo interior with city skyline view">
          <polygon class="hex-frame" fill="url(#interior)" points="770,32 844.5,75 844.5,161 770,204 695.5,161 695.5,75"/>
        </g>
        <g role="img" aria-label="Photo of an empty room with large windows">
          <polygon class="hex-frame" fill="url(#interior)" points="919,32 993.5,75 993.5,161 919,204 844.5,161 844.5,75"/>
        </g>
        <g role="img" aria-label="Photo of a brick residential tower">
          <polygon class="hex-frame" fill="url(#tower)" points="1068,32 1142.5,75 1142.5,161 1068,204 993.5,161 993.5,75"/>
        </g>
        <g role="img" aria-label="Photo of a window corner overlooking the city">
          <polygon class="hex-frame" fill="url(#interior)" points="695.5,180 756,215 756,285 695.5,320 635,285 635,215"/>
        </g>
        <g role="img" aria-label="Photo of a blue glass apartment building">
          <polygon class="hex-frame" fill="url(#facade)" points="844.5,161 919,204 919,290 844.5,333 770,290 770,204"/>
        </g>
        <g role="img" aria-label="Photo of a blue mid-rise building at street level">
          <polygon class="hex-frame" fill="url(#facade)" points="993.5,161 1068,204 1068,290 993.5,333 919,290 919,204"/>
        </g>
        <g role="img" aria-label="Small photo of a bright interior">
          <polygon class="hex-frame" fill="url(#interior)" points="650,74 678,90 678,122 650,138 622,122 622,90"/>
        </g>
        <g role="img" aria-label="Small photo of a building facade">
          <polygon fill="url(#tower)" points="676,162 689,170 689,185 676,193 663,185 663,170"/>
        </g>
      </g>
    </svg>

    <div class="brand">
      <div class="brand-mark"></div>
      <p class="brand-name">VERANTA<small>ARCHITECTURAL SYSTEMS</small></p>
    </div>

    <div class="identity">
      <p class="identity-name">Morbe Vatki</p>
      <div class="identity-role"><h1>FOUNDER</h1><span class="rule"></span></div>
      <p class="identity-site">VerantaStudio.example</p>
      <ul class="identity-points">
        <li>Green Building Technologies Innovator<span>|</span></li>
        <li>15+ Years Work Experience<span>|</span></li>
        <li>BCom. at Northlake University<span>|</span></li>
        <li>Contact Me For Green Buildings Soulutions</li>
      </ul>
      <div class="social">
        <span class="social-item"><i></i>WWW.SITE.EXAMPLE</span>
        <span class="social-item"><i></i>CIRCLEBOOK</span>
        <span class="social-item"><i></i>PHOTOFEED</span>
        <span class="social-item"><i></i>VIDSTREAM</span>
      </div>
    </div>
  </section>
</body>
</html>
```